Property Management Company

We are looking for a sharp/modern business card design for a property management company.
We have included what should be on the business card down below in business card details.
Target Market(s)
Commercial properties, Home Owners
Industry/Entity Type
Business
Contact Information for Business Card
Name: Colin Basford | Owner
Business Name : Tern Yardworks
Slogan : A Smarter Choice
Phone : 518.555.0183
Website: www.ternyardworks.example
E-Mail : colin@ternyardworks.example
Our Services are Commercial & Residential
-Asphalt Maintenance
-Snow Management
-Landscaping
-Blacktop
Free Estimates
Free parking lot cleanup & restripe with snow removal contract

```html
<!DOCTYPE html>
<html lang="en">
<head>
<meta charset="utf-8">
<title>Tern Yardworks – Business Card</title>
<link href="https://fonts.googleapis.com/css2?family=Open+Sans:ital,wght@0,400;0,600;0,700;0,800;1,600;1,700&display=swap" rel="stylesheet">
<style>
  :root {
    --stage: #000000;
    --red: #b91f2c;
    --red-dark: #a41b26;
    --navy: #1b2a4e;
    --green: #1e7f3a;
    --ink: #1f1f1f;
    --card-white: #f6f6f6;
    --white: #ffffff;
  }
  * { box-sizing: border-box; margin: 0; padding: 0; }
  html, body {
    width: 1200px; height: 1000px; overflow: hidden;
    background: var(--stage);
    font-family: "Open Sans", Arial, sans-serif;
  }
  .canvas { position: relative; width: 1200px; height: 1000px; }
  .card {
    position: absolute; left: 260px; width: 680px; height: 386px;
    border-radius: 22px; overflow: hidden;
  }
  .card-front {
    top: 88px;
    background: linear-gradient(180deg, var(--red) 0%, var(--red-dark) 100%);
    display: flex; flex-direction: column; align-items: center; justify-content: center;
    color: var(--white); text-align: center;
  }
  .front-name {
    font-weight: 800; font-size: 62px; line-height: 1.05; letter-spacing: 1px;
    text-transform: uppercase; color: var(--white);
  }
  .front-mark { width: 22px; height: 22px; background: var(--white); margin-bottom: 22px; }
  .front-sub { font-weight: 700; font-size: 25px; margin-top: 14px; }
  .front-slogan { font-weight: 700; font-style: italic; font-size: 19px; margin-top: 14px; letter-spacing: 0.3px; }

  .card-back { top: 528px; background: var(--card-white); }
  .back-brand {
    position: absolute; left: 30px; top: 40px; width: 300px; height: 170px;
    display: flex; flex-direction: column; align-items: center; justify-content: center; text-align: center;
  }
  .brand-mark { width: 18px; height: 18px; background: var(--red); margin-bottom: 14px; }
  .brand-name {
    font-weight: 800; font-size: 38px; line-height: 1.05; text-transform: uppercase; color: var(--navy);
  }
  .brand-sub { font-weight: 700; font-size: 19px; color: var(--green); margin-top: 10px; }
  .divider { position: absolute; left: 338px; top: 43px; width: 2px; height: 164px; background: var(--ink); }
  .contact { position: absolute; left: 400px; top: 62px; color: var(--ink); }
  .contact-name { font-weight: 700; font-size: 23px; letter-spacing: 0.3px; text-transform: uppercase; line-height: 1.1; }
  .contact-role { font-weight: 600; font-style: italic; font-size: 17px; color: var(--green); line-height: 1.2; }
  .contact-list { list-style: none; margin-top: 14px; }
  .contact-list li { display: flex; align-items: center; gap: 8px; font-size: 17px; font-weight: 600; height: 24px; }
  .contact-list svg { width: 15px; height: 15px; fill: var(--green); flex: none; }

  .services { position: absolute; left: 12px; right: 12px; top: 239px; }
  .services-head {
    height: 36px; background: var(--navy); color: var(--white);
    border-radius: 12px 12px 0 0; text-align: center;
    font-weight: 700; font-size: 16px; letter-spacing: 1px; line-height: 38px;
  }
  .services-body {
    margin-top: 4px; height: 97px; background: var(--red); border-radius: 0 0 12px 12px;
    color: var(--white); padding-top: 6px;
  }
  .service-row { display: flex; justify-content: center; gap: 14px; height: 29px; align-items: center; }
  .service { font-style: italic; font-weight: 600; font-size: 16px; display: flex; align-items: center; gap: 4px; }
  .service svg { width: 17px; height: 14px; fill: none; stroke: var(--navy); stroke-width: 3; }
</style>
</head>
<body>
<div class="canvas">
  <section class="card card-front">
    <div class="front-mark"></div>
    <div class="front-name">Tern Yardworks</div>
    <div class="front-sub">Property Management</div>
    <div class="front-slogan">A SMARTER CHOICE</div>
  </section>

  <section class="card card-back">
    <div class="back-brand">
      <div class="brand-mark"></div>
      <div class="brand-name">Tern<br>Yardworks</div>
      <div class="brand-sub">Property Management</div>
    </div>
    <div class="divider"></div>
    <div class="contact">
      <div class="contact-name">Colin Basford</div>
      <div class="contact-role">Owner</div>
      <ul class="contact-list">
        <li><svg viewBox="0 0 16 16"><path d="M4 1h8a1 1 0 0 1 1 1v12a1 1 0 0 1-1 1H4a1 1 0 0 1-1-1V2a1 1 0 0 1 1-1zm1 2v9h6V3z"/></svg>518.555.0183</li>
        <li><svg viewBox="0 0 16 16"><path d="M1 3h14v10H1zm2 2 5 4 5-4v-0.5H3zm0 2v4h10V7l-5 4z"/></svg>colin@ternyardworks.example</li>
        <li><svg viewBox="0 0 16 16"><path d="M8 1a7 7 0 1 0 0 14A7 7 0 0 0 8 1zm0 1.5c.8 0 1.7 1.6 2 4H6c.3-2.4 1.2-4 2-4zM2.6 6.5h2C4.5 7 4.5 7.5 4.5 8s0 1 .1 1.5h-2a5.6 5.6 0 0 1 0-3zm8.8 0h2a5.6 5.6 0 0 1 0 3h-2c.1-.5.1-1 .1-1.5s0-1-.1-1.5zM6 9.5h4c-.3 2.4-1.2 4-2 4s-1.7-1.6-2-4z"/></svg>www.ternyardworks.example</li>
      </ul>
    </div>

    <div class="services">
      <div class="services-head">OUR SERVICES</div>
      <div class="services-body">
        <div class="service-row">
          <span class="service">Commercial &amp; Residential <svg viewBox="0 0 17 14"><path d="M2 7l4 4 9-9"/></svg></span>
          <span class="service">Asphalt Repair <svg viewBox="0 0 17 14"><path d="M2 7l4 4 9-9"/></svg></span>
          <span class="service">Sealcoating <svg viewBox="0 0 17 14"><path d="M2 7l4 4 9-9"/></svg></span>
        </div>
        <div class="service-row">
          <span class="service">Snow Management <svg viewBox="0 0 17 14"><path d="M2 7l4 4 9-9"/></svg></span>
          <span class="service">Landscaping <svg viewBox="0 0 17 14"><path d="M2 7l4 4 9-9"/></svg></span>
          <span class="service">Concrete <svg viewBox="0 0 17 14"><path d="M2 7l4 4 9-9"/></svg></span>
          <span class="service">Free Estimates <svg viewBox="0 0 17 14"><path d="M2 7l4 4 9-9"/></svg></span>
        </div>
        <div class="service-row">
          <span class="service">Free parking lot cleanup &amp; restripe with snow removal contract <svg viewBox="0 0 17 14"><path d="M2 7l4 4 9-9"/></svg></span>
        </div>
      </div>
    </div>
  </section>
</div>
</body>
</html>
```